Varrow Kestin military/warrior themed clothing company**

eCommerce clothing website

We do have a Shopify account that we would ups like this to be built on for it obvious reasons

We will be starting with the gym/casual wear “Varrow” it will be military style with a unique logo as well as military colours. We will sell this as an exclusive range limited edition to create a scarcity principle which hopefully has our customer desperate to get their gear. We will have it in the colours that Army, Navy and Airforce wear as their undershirts and PT shirts as this will create some great genuine military and KBMQ Security origins. Exclusivity is the key.

Having a similar business model and advertising as LiftOtter who have done incredibly well in this area. Our story is better and we just study what sells and how they sell it. Focused on tops namely shirts and singlet and not 1000 choices keep it simple as simple is best and it sells.

Our story

• Veteran Security Company that requires our staff to keep in shape to provide the community with the best service
• No other brands or designers were up to the task of our military styled training, it all thinned, ripped, and looked terrible
• Decided if it’s broken, fix it and do it ourselves
• Trialed and tested every material and design on the market with extensive hours in the gym, outdoor PT, beach sessions, hill runs, boot camps, go till you puke and we did
• Found what worked and put it into action with a limited order just for our staff
• Some of the boys are still servicing and wore the gear to base PT and their fellow serving members wanted to get some of their own gear to which me made limited orders
• Created purpose PT gear with suitable colour scheme to conform with military regs so the boys no longer got in trouble, made limited orders
• Friends and family really liked the gear so after relentless persistence we gave in and made limited orders
• While performing volunteer advocacy work at the VAFs fellow veterans loved the designs and begged for their own gear which would give them confidence and motivation to get back in the gym to rehabilitate and get their health back, it was a no brainer we made limited order
• We began sponsoring local up and coming athletes, fighters and body builders so they could pursue their dream of becoming a professional in their craft again limited orders were made
• Though more relentless desire to obtain our brand and come onboard with our mission statement influencers and celebrities a like urged to endorse and become brand ambassadors so every Australian could feel what it was like to be apart of a genuine grass roots community that had a great story behind it
• And with that Varrow was born
• Stay tuned for the next exciting instalment of what’s to come as we don’t believe in reinventing the wheel but smashing it down completely

A comprehensive range that targets men and women of all ages, fitness levels, body shapes and their specific needs for all times with an exclusive veterans range to support the veteran community.

Top gym brands
Lift otter
VORN
Pale lantern
Qova
Brelto
Fandry

Target Market(s)

men and women 30-45

Industry/Entity Type

Clothing

Number of Pages Required

5+ page

Font styles to use
Sans Serif

Requirements
Must have
• Home page
• white clean back ground
• menu in the top right corner
• search function
• Varrow lettering up the top nice and clean in black
• crisp Varrow shot of the first shoot in both the black and white gold
• headline "forge your legacy" comes across the bottom of the shot above
• men's lifestyle wear section - pre-order now - hyperlink to casual section
• men's active wear section - pre-order now - hyperlink to fitness section
• women's range - coming soon - hyperlink to women's section
• socials and contact (Facebook, Instagram)

Page 2
• our mission
• our story
• our values

Page 3
Change to lifestyle
Follow the format below for order
Functionality to allow pre-order sales for out of stock units

• men's casual wear
- casual singlets
- casual tees
- casual crews
- casual hoodies
- pre-order now

Page 4
Change to active wear

• men's fitness wear
- fitness tees
- fitness crews
- fitness hoodies
- pre-order now

Page 5
• women's section
- coming soon

Australian owed
Australian made
Australian benefit

Throw in an Australian flag

The whole idea was to be bringing in pre-order sales as we wait for the first order to come in from supplier and the next photo shoot we can simply update all the stock pics as needed. For now I have the tec-pac pics that can go in the product pages.

Mission

Building an unstoppable force of warriors that strive for perfection in every aspect of their lives to forge a legacy

Concept

Varrow is an unstoppable force that protect and inspire their own.

Varrow clothing is battle armour to wear as you take the hardest aspects of life to task.

From our struggle comes our resolve.

Tribute

Our fallen warriors and heroes that have come before us, making the ultimate sacrifice, that has allowed our lives to be free and liberated for an unencumbered pursuit of happiness

Story
• Australian family owned and operated
• Veteran led and staffed
• Created to protect those who protect us
• Tried and tested under military conditions
• Australian sourced and produced
• Ethical and environmentally friendly materials
• Restoration of Australian Pride

Values
• Culture
• Community
• Patriotism
• Honour
• Honesty
• Integrity
• Loyalty
• Courage
• Team work
• Success
Nice to have
• To look and feel like one of the big competitors with ease of navigation and ordering
Should not have
• clutter and loading issues

```html
<!DOCTYPE html>
<html lang="en">
<head>
<meta charset="utf-8">
<title>Varrow — Forge Your Legacy</title>
<link href="https://fonts.googleapis.com/css2?family=DM+Serif+Display&family=Lora:wght@400;500;600&family=Lato:wght@400;700&display=swap" rel="stylesheet">
<style>
:root{
  --ink:#1b1b1b;
  --bronze:#8a7252;
  --olive:#6e7a52;
  --gold:#c6b386;
  --blue:#1f69b5;
  --star:#f5b50a;
  --paper:#f5f4f0;
  --band:#f7f6f3;
  --night:#0e0e0e;
  --rule:#2a2a2a;
  --white:#ffffff;
}
*{box-sizing:border-box;margin:0;padding:0}
html,body{width:1200px;height:3717px;overflow:hidden;background:var(--white)}
body{position:relative;font-family:"Lato",sans-serif;color:var(--ink)}
.abs{position:absolute}
a{color:inherit;text-decoration:none}
h1,h2,h3,h4{font-weight:400}

/* header & hero */
.hero-bg{left:0;top:0;width:1200px;height:660px;background:linear-gradient(180deg,var(--paper) 0%,var(--paper) 80%,var(--white) 100%)}
.nav a{position:absolute;top:58px;font-family:"Lora",serif;font-size:13px;font-weight:500}
.brand{width:160px;text-align:center;font-family:"Lora",serif;font-size:26px;font-weight:500;letter-spacing:3px;line-height:1}
.tools{left:850px;top:48px}
.hero-title{left:183px;top:165px;font-family:"DM Serif Display",serif;font-size:62px;line-height:72px;color:var(--bronze)}
.hero-copy{left:183px;top:346px;width:355px;font-size:13px;line-height:25px;color:#333}
.btn{display:flex;align-items:center;justify-content:center;background:var(--olive);color:var(--white);font-family:"Lora",serif;font-weight:600;font-size:14px;border-radius:3px}
.play{left:312px;top:468px;width:36px;height:36px;border-radius:50%;border:1.5px solid var(--olive);background:var(--white);display:flex;align-items:center;justify-content:center}
.whats-new{left:368px;top:478px;font-family:"Lora",serif;font-size:13px;color:var(--bronze)}
.social-dot{width:34px;height:34px;border-radius:50%;border:1px solid #555;display:flex;align-items:center;justify-content:center}
.hero-disc{left:642px;top:187px;width:346px;height:346px;border-radius:50%;background:var(--gold)}
.hero-model{left:728px;top:94px;width:212px;height:460px;border-radius:100px 100px 12px 12px;background:linear-gradient(180deg,#7d6b4d 0%,#6f6a45 55%,#5d5a3c 100%)}
.float-card{background:var(--white);border-radius:4px;box-shadow:0 6px 18px rgba(0,0,0,.1);overflow:hidden}
.float-photo{height:90px;background:linear-gradient(180deg,#dad7ce,#c9c3b2)}
.float-title{font-family:"Lora",serif;font-size:9px;text-align:center;margin-top:10px}
.float-row{display:flex;justify-content:space-between;align-items:center;padding:6px 12px 0;font-family:"Lora",serif;font-size:11px;color:var(--bronze)}
.like{left:999px;top:154px;width:36px;height:36px;border-radius:50%;background:#dbe9f6;display:flex;align-items:center;justify-content:center}
.avatars{left:623px;top:418px;width:159px;height:49px;background:var(--white);border-radius:6px;box-shadow:0 6px 18px rgba(0,0,0,.1);display:flex;align-items:center;justify-content:center}
.avatar{width:26px;height:26px;border-radius:50%;background:#8a7760;border:2px solid var(--white);margin-left:-6px}
.heart-bubble{left:686px;top:485px;width:36px;height:36px;border-radius:50%;background:#f6d9d9;display:flex;align-items:center;justify-content:center}

/* section heads */
.section-title{font-family:"DM Serif Display",serif;font-size:37px;color:var(--bronze)}
.section-copy{font-size:13px;line-height:25px;color:#444;width:400px}
.tab{font-family:"Lora",serif;font-size:15px;color:#555;padding-bottom:4px}
.tab.active{border-bottom:1.5px solid #555}
.arrow{width:40px;height:40px;border-radius:50%;display:flex;align-items:center;justify-content:center}
.arrow.prev{background:var(--white);box-shadow:0 3px 10px rgba(0,0,0,.12)}
.arrow.next{background:var(--olive)}

/* product card */
.product{width:263px}
.product-photo{position:relative;height:310px;background:linear-gradient(180deg,#f2f2f2 0%,#e7e5e2 100%);border-radius:2px;overflow:hidden}
.product-photo .figure{position:absolute;left:50%;bottom:0;width:150px;height:270px;transform:translateX(-50%);border-radius:70px 70px 0 0;background:linear-gradient(180deg,#c8b8a8 0%,#9e9a97 40%,#8f9399 100%)}
.badge{position:absolute;right:26px;top:0;width:58px;height:31px;background:var(--blue);color:var(--white);font-family:"Lora",serif;font-size:13px;text-align:center;padding-top:5px;clip-path:polygon(0 0,100% 0,100% 75%,50% 100%,0 75%)}
.quick{position:absolute;left:0;top:0;width:84px;height:310px;background:var(--gold)}
.sizes{position:absolute;left:84px;top:87px;width:41px;height:190px;background:var(--white);border-radius:3px;font-family:"Lora",serif;font-size:13px;color:#444;display:flex;flex-direction:column;justify-content:space-around;align-items:center;padding:6px 0}
.quick-btn{position:absolute;left:14px;width:54px;height:54px;border-radius:50%;background:var(--white);display:flex;align-items:center;justify-content:center}
.product-name{margin:22px 0 0 8px;font-family:"Lora",serif;font-size:15px;font-weight:400;white-space:nowrap}
.product-meta{display:flex;justify-content:space-between;align-items:center;margin:10px 6px 0 8px}
.price{font-family:"Lora",serif;font-size:17px}
.price small{font-size:11px;margin-right:2px}
.more{display:inline-flex;align-items:center;gap:6px;margin:14px 0 0 8px;font-family:"Lora",serif;font-size:13px;font-weight:600;color:var(--blue)}

/* category band */
.band{left:0;top:1861px;width:1200px;height:562px;background:var(--band)}
.cat{width:263px;height:382px;overflow:hidden;background:#ededed}
.cat-photo{height:309px}
.cat-label{height:73px;display:flex;align-items:center;justify-content:center;font-family:"DM Serif Display",serif;font-size:36px;color:var(--white);letter-spacing:1px}

/* footer */
.footer{left:0;top:3221px;width:1200px;height:496px;background:var(--night)}
.foot-text{position:absolute;color:var(--white);font-family:"Lora",serif;font-size:12px;font-weight:600}
.foot-small{font-size:11px;line-height:16px}
.newsletter{left:248px;top:3285px;font-family:"DM Serif Display",serif;font-size:27px;color:var(--white)}
.field{left:661px;top:3275px;width:236px;height:49px;background:var(--white);border-radius:3px 0 0 3px;font-size:9px;color:#999;padding:20px 0 0 16px}
.bell{left:897px;top:3275px;width:55px;height:49px;background:var(--olive);border-radius:0 3px 3px 0;display:flex;align-items:center;justify-content:center}
.foot-dot{width:22px;height:22px;border-radius:50%;background:var(--olive);display:flex;align-items:center;justify-content:center}
</style>
</head>
<body>
<svg width="0" height="0" style="position:absolute">
  <defs>
    <symbol id="star" viewBox="0 0 20 20"><polygon points="10,1 12.6,7 19,7.4 14,11.6 15.6,18 10,14.5 4.4,18 6,11.6 1,7.4 7.4,7"/></symbol>
    <symbol id="arrow-right" viewBox="0 0 14 10"><path d="M1 5h11M8 1l4 4-4 4" fill="none" stroke="currentColor" stroke-width="1.2"/></symbol>
    <symbol id="heart" viewBox="0 0 24 22"><path d="M12 21 2.5 11.5A5.5 5.5 0 0 1 12 4a5.5 5.5 0 0 1 9.5 7.5Z" fill="#e0393e"/></symbol>
    <symbol id="cart" viewBox="0 0 24 24"><path d="M2 4h3l2.4 11h11l2-8H6.2" fill="none" stroke="#222" stroke-width="1.6"/><circle cx="9" cy="19" r="1.6" fill="#222"/><circle cx="17" cy="19" r="1.6" fill="#222"/></symbol>
    <symbol id="compare" viewBox="0 0 24 24"><rect x="4" y="4" width="12" height="10" rx="1.5" fill="none" stroke="#222" stroke-width="1.5"/><rect x="8" y="9" width="12" height="10" rx="1.5" fill="#fff" stroke="#222" stroke-width="1.5"/></symbol>
    <symbol id="rating4" viewBox="0 0 86 15"><g fill="#f5b50a"><use href="#star" x="0" width="15" height="15"/><use href="#star" x="18" width="15" height="15"/><use href="#star" x="36" width="15" height="15"/><use href="#star" x="54" width="15" height="15"/></g><use href="#star" x="72" width="15" height="15" fill="#bdbdbd"/></symbol>
    <symbol id="rating5" viewBox="0 0 50 9"><g fill="#f5b50a"><use href="#star" x="0" width="9" height="9"/><use href="#star" x="10" width="9" height="9"/><use href="#star" x="20" width="9" height="9"/><use href="#star" x="30" width="9" height="9"/><use href="#star" x="40" width="9" height="9"/></g></symbol>
  </defs>
</svg>

<!-- Hero -->
<div class="abs hero-bg"></div>
<nav class="nav">
  <a style="left:183px">Home</a>
  <a style="left:255px">Men</a>
  <a style="left:316px">Women</a>
  <a style="left:400px">About Us</a>
</nav>
<div class="abs brand" style="left:520px;top:42px">VARROW</div>
<div class="abs tools">
  <svg width="170" height="26" viewBox="0 0 170 26">
    <circle cx="14" cy="11" r="6" fill="none" stroke="#222" stroke-width="1.6"/><path d="M18.5 15.5 23 20" stroke="#222" stroke-width="1.6"/>
    <path d="M40 3v20" stroke="#222" stroke-width="1"/>
    <use href="#cart" x="54" y="1" width="22" height="22"/>
    <text x="76" y="22" font-size="8" font-family="Lato,sans-serif">00</text>
    <circle cx="110" cy="12" r="9" fill="none" stroke="#222" stroke-width="1.4"/><circle cx="110" cy="10" r="3" fill="none" stroke="#222" stroke-width="1.4"/><path d="M104 18c2-3 10-3 12 0" fill="none" stroke="#222" stroke-width="1.4"/>
    <path d="M138 5h26M142 12h22M138 19h26" stroke="#111" stroke-width="3.4"/>
  </svg>
</div>

<div class="abs social-dot" style="left:74px;top:277px"><svg width="12" height="12" viewBox="0 0 12 12"><text x="6" y="10" text-anchor="middle" font-size="10" font-family="Lato,sans-serif" font-weight="700">f</text></svg></div>
<div class="abs social-dot" style="left:74px;top:335px"><svg width="12" height="12" viewBox="0 0 12 12"><rect x="1.5" y="1.5" width="9" height="9" rx="2.5" fill="none" stroke="#222"/><circle cx="6" cy="6" r="2" fill="none" stroke="#222"/></svg></div>

<h1 class="abs hero-title">Forge Your<br>Legacy</h1>
<p class="abs hero-copy">Lorem ipsum dolor sit amet, consectetur adipiscing elit, sed do eiusmod tempor incididunt ut labore et dolore magna aliqua. Quis ipsum suspendisse ultrices gravida.</p>
<a class="abs btn" style="left:183px;top:460px;width:104px;height:51px">Shop</a>
<div class="abs play"><svg width="10" height="10" viewBox="0 0 10 10"><polygon points="2,1 9,5 2,9" fill="#6e7a52"/></svg></div>
<span class="abs whats-new">What's New</span>

<div class="abs hero-disc"></div>
<div class="abs hero-model" role="img" aria-label="Bearded man in camouflage jacket and scarf, arms crossed"></div>
<div class="abs like"><svg width="16" height="16" viewBox="0 0 16 16"><path d="M2 7h3v7H2zM6 7l3-5c1.5 0 1.8 1 1.5 2.5L10 6h3.2c.9 0 1.4.8 1.2 1.6l-1.3 5c-.2.8-.8 1.4-1.6 1.4H6z" fill="#1f69b5"/></svg></div>

<div class="abs float-card" style="left:564px;top:185px;width:161px;height:148px">
  <div class="float-photo" role="img" aria-label="Man in grey gym t-shirt"></div>
  <div class="float-title">Men's T-Shirt</div>
  <div class="float-row"><span>$ 25.00</span><svg width="50" height="9"><use href="#rating5" width="50" height="9"/></svg></div>
</div>
<div class="abs float-card" style="left:927px;top:371px;width:160px;height:148px">
  <div class="float-photo" role="img" aria-label="Woman in grey sports bra flexing"></div>
  <div class="float-title">Women's T-Shirt</div>
  <div class="float-row"><span>$ 26.03</span><svg width="50" height="9"><use href="#rating5" width="50" height="9"/></svg></div>
</div>
<div class="abs avatars" role="img" aria-label="Row of customer portraits">
  <span class="avatar" style="margin-left:0"></span><span class="avatar" style="background:#3f3a34"></span><span class="avatar" style="background:#a68a6d"></span><span class="avatar" style="background:#57493b"></span><span class="avatar" style="background:#b79a7c"></span><span class="avatar" style="background:#6c5a47"></span>
</div>
<div class="abs heart-bubble"><svg width="18" height="16"><use href="#heart" width="18" height="16"/></svg></div>

<!-- Latest collection -->
<h2 class="abs section-title" style="left:183px;top:678px">Our Letest Collection</h2>
<p class="abs section-copy" style="left:183px;top:745px">Lorem ipsum dolor sit amet, consectetur adipiscing elit, sed do eiusmod tempor incididunt ut labore.</p>
<span class="abs tab active" style="left:753px;top:771px">Men</span>
<span class="abs tab" style="left:820px;top:771px">Women</span>
<div class="abs arrow prev" style="left:920px;top:762px"><svg width="10" height="12"><path d="M7 1 2 6l5 5" fill="none" stroke="#222" stroke-width="1.5"/></svg></div>
<div class="abs arrow next" style="left:975px;top:762px"><svg width="10" height="12"><path d="M3 1l5 5-5 5" fill="none" stroke="#fff" stroke-width="1.5"/></svg></div>

<article class="abs product" style="left:183px;top:867px">
  <div class="product-photo">
    <div class="figure" role="img" aria-label="Man in grey gym t-shirt, arms crossed"></div>
    <div class="quick"></div>
    <div class="quick-btn" style="top:48px"><svg width="22" height="20"><use href="#heart" width="22" height="20"/></svg></div>
    <div class="quick-btn" style="top:133px"><svg width="22" height="22"><use href="#cart" width="22" height="22"/></svg></div>
    <div class="quick-btn" style="top:217px"><svg width="22" height="22"><use href="#compare" width="22" height="22"/></svg></div>
    <div class="sizes"><span>S</span><span>L</span><span>M</span><span>XL</span><span>XXL</span></div>
  </div>
  <h3 class="product-name">Qova Men's Gym T-shirt</h3>
  <div class="product-meta"><span class="price"><small>$</small>20.06</span><svg width="86" height="15"><use href="#rating4" width="86" height="15"/></svg></div>
  <a class="more">More Details <svg width="14" height="10"><use href="#arrow-right" width="14" height="10"/></svg></a>
</article>

<article class="abs product" style="left:469px;top:867px">
  <div class="product-photo"><div class="figure" role="img" aria-label="Muscular man in white tank top" style="background:linear-gradient(180deg,#d6b79f 0%,#f4f4f4 40%,#2f3544 100%)"></div><span class="badge">New</span></div>
  <h3 class="product-name">Lift Otter Men's PT T-shirt</h3>
  <div class="product-meta"><span class="price"><small>$</small>19.02</span><svg width="86" height="15"><use href="#rating4" width="86" height="15"/></svg></div>
  <a class="more">More Details <svg width="14" height="10"><use href="#arrow-right" width="14" height="10"/></svg></a>
</article>

<article class="abs product" style="left:753px;top:867px">
  <div class="product-photo"><div class="figure" role="img" aria-label="Smiling man in grey t-shirt"></div><span class="badge">New</span></div>
  <h3 class="product-name">VORN Men's Gym T-shirt</h3>
  <div class="product-meta"><span class="price"><small>$</small>20.02</span><svg width="86" height="15"><use href="#rating4" width="86" height="15"/></svg></div>
  <a class="more">More Details <svg width="14" height="10"><use href="#arrow-right" width="14" height="10"/></svg></a>
</article>

<article class="abs product" style="left:183px;top:1337px">
  <div class="product-photo"><div class="figure" role="img" aria-label="Man in white tank top, arms crossed" style="background:linear-gradient(180deg,#d6b79f 0%,#f4f4f4 40%,#e8e8e8 100%)"></div><span class="badge">New</span></div>
  <h3 class="product-name">Lift Otter Men's PT T-shirt</h3>
  <div class="product-meta"><span class="price"><small>$</small>19.02</span><svg width="86" height="15"><use href="#rating4" width="86" height="15"/></svg></div>
  <a class="more">More Details <svg width="14" height="10"><use href="#arrow-right" width="14" height="10"/></svg></a>
</article>

<article class="abs product" style="left:469px;top:1337px">
  <div class="product-photo"><div class="figure" role="img" aria-label="Man in black t-shirt giving thumbs up" style="background:linear-gradient(180deg,#c9a58a 0%,#1d1d1d 35%,#151515 100%)"></div><span class="badge">New</span></div>
  <h3 class="product-name">VORN Men's Gym T-shirt</h3>
  <div class="product-meta"><span class="price"><small>$</small>20.02</span><svg width="86" height="15"><use href="#rating4" width="86" height="15"/></svg></div>
  <a class="more">More Details <svg width="14" height="10"><use href="#arrow-right" width="14" height="10"/></svg></a>
</article>

<article class="abs product" style="left:753px;top:1337px">
  <div class="product-photo"><div class="figure" role="img" aria-label="Man in grey t-shirt, arms crossed"></div><span class="badge">New</span></div>
  <h3 class="product-name">Lift Otter Men's PT T-shirt</h3>
  <div class="product-meta"><span class="price"><small>$</small>19.02</span><svg width="86" height="15"><use href="#rating4" width="86" height="15"/></svg></div>
  <a class="more">More Details <svg width="14" height="10"><use href="#arrow-right" width="14" height="10"/></svg></a>
</article>

<!-- Categories -->
<div class="abs band"></div>
<a class="abs cat" style="left:183px;top:1950px">
  <div class="cat-photo" role="img" aria-label="Man in black t-shirt giving thumbs up" style="background:linear-gradient(180deg,#ececec 0%,#2a2a2a 60%,#1a1a1a 100%)"></div>
  <div class="cat-label" style="background:var(--blue)">Men</div>
</a>
<a class="abs cat" style="left:469px;top:1950px">
  <div class="cat-photo" role="img" aria-label="Woman in grey sports bra flexing, wearing headphones" style="background:linear-gradient(180deg,#ececec 0%,#b08a6c 45%,#7b7b7b 100%)"></div>
  <div class="cat-label" style="background:var(--gold)">Women</div>
</a>
<h2 class="abs section-title" style="left:753px;top:2052px;line-height:49px">Get The Best<br>Product</h2>
<p class="abs section-copy" style="left:753px;top:2169px;width:250px">Lorem ipsum dolor sit amet, consectetur adipiscing elit, sed do eiusmod tempor incididunt ut labore.</p>
<a class="abs btn" style="left:753px;top:2280px;width:121px;height:52px">Explore</a>

<!-- Popular collection -->
<h2 class="abs section-title" style="left:183px;top:2503px">Our Popular Collection</h2>
<p class="abs section-copy" style="left:183px;top:2570px">Lorem ipsum dolor sit amet, consectetur adipiscing elit, sed do eiusmod tempor incididunt ut labore.</p>
<span class="abs tab" style="left:753px;top:2594px">Men</span>
<span class="abs tab active" style="left:820px;top:2594px">Women</span>
<div class="abs arrow prev" style="left:920px;top:2585px"><svg width="10" height="12"><path d="M7 1 2 6l5 5" fill="none" stroke="#222" stroke-width="1.5"/></svg></div>
<div class="abs arrow next" style="left:975px;top:2585px"><svg width="10" height="12"><path d="M3 1l5 5-5 5" fill="none" stroke="#fff" stroke-width="1.5"/></svg></div>

<article class="abs product" style="left:183px;top:2691px">
  <div class="product-photo">
    <div class="figure" role="img" aria-label="Woman in grey sports bra with headphones" style="background:linear-gradient(180deg,#9a7256 0%,#8a8a8a 45%,#b8a98c 100%)"></div>
    <div class="quick"></div>
    <div class="quick-btn" style="top:48px"><svg width="22" height="20"><use href="#heart" width="22" height="20"/></svg></div>
    <div class="quick-btn" style="top:133px"><svg width="22" height="22"><use href="#cart" width="22" height="22"/></svg></div>
    <div class="quick-btn" style="top:217px"><svg width="22" height="22"><use href="#compare" width="22" height="22"/></svg></div>
    <div class="sizes"><span>S</span><span>L</span><span>M</span><span>XL</span><span>XXL</span></div>
  </div>
  <h3 class="product-name">Qova Women's Gym T-shirt</h3>
  <div class="product-meta"><span class="price"><small>$</small>20.06</span><svg width="86" height="15"><use href="#rating4" width="86" height="15"/></svg></div>
  <a class="more">More Details <svg width="14" height="10"><use href="#arrow-right" width="14" height="10"/></svg></a>
</article>

<article class="abs product" style="left:469px;top:2691px">
  <div class="product-photo"><div class="figure" role="img" aria-label="Woman in black sports bra, hands in hair" style="background:linear-gradient(180deg,#d2b08e 0%,#1e1e1e 45%,#d9b99a 70%,#222 100%)"></div></div>
  <h3 class="product-name">Lift Otter Women's PT T-shirt</h3>
  <div class="product-meta"><span class="price"><small>$</small>19.02</span><svg width="86" height="15"><use href="#rating4" width="86" height="15"/></svg></div>
  <a class="more">More Details <svg width="14" height="10"><use href="#arrow-right" width="14" height="10"/></svg></a>
</article>

<article class="abs product" style="left:753px;top:2691px">
  <div class="product-photo"><div class="figure" role="img" aria-label="Woman in grey sports bra flexing" style="background:linear-gradient(180deg,#9a7256 0%,#8a8a8a 45%,#2a2a2a 100%)"></div></div>
  <h3 class="product-name">VORN Women's Gym T-shirt</h3>
  <div class="product-meta"><span class="price"><small>$</small>20.02</span><svg width="86" height="15"><use href="#rating4" width="86" height="15"/></svg></div>
  <a class="more">More Details <svg width="14" height="10"><use href="#arrow-right" width="14" height="10"/></svg></a>
</article>

<article class="abs product" style="left:1038px;top:2691px">
  <div class="product-photo"><div class="figure" role="img" aria-label="Woman in black sports bra, hands in hair" style="background:linear-gradient(180deg,#d2b08e 0%,#1e1e1e 45%,#d9b99a 70%,#222 100%)"></div></div>
  <h3 class="product-name">Lift Otter Women's PT T-shirt</h3>
  <div class="product-meta"><span class="price"><small>$</small>19.02</span></div>
  <a class="more">More Details <svg width="14" height="10"><use href="#arrow-right" width="14" height="10"/></svg></a>
</article>

<!-- Footer -->
<footer class="abs footer"></footer>
<h2 class="abs newsletter">Subscribe Our Newsletter</h2>
<div class="abs field">Enter Your Email</div>
<div class="abs bell"><svg width="22" height="22" viewBox="0 0 22 22"><path d="M5 16V10a6 6 0 0 1 12 0v6l2 2H3z" fill="none" stroke="#fff" stroke-width="1.4"/><path d="M9 19a2 2 0 0 0 4 0" fill="none" stroke="#fff" stroke-width="1.4"/></svg></div>
<div class="abs" style="left:450px;top:3378px;width:567px;height:1px;background:var(--rule)"></div>

<div class="abs brand" style="left:222px;top:3498px;color:var(--white);font-size:30px">VARROW</div>

<h4 class="foot-text" style="left:469px;top:3440px">Information</h4>
<h4 class="foot-text" style="left:754px;top:3440px">Contact Us</h4>
<a class="foot-text" style="left:469px;top:3498px">Home</a>
<a class="foot-text" style="left:469px;top:3529px">Men</a>
<a class="foot-text" style="left:469px;top:3560px">Women</a>
<a class="foot-text" style="left:469px;top:3592px">About us</a>
<a class="foot-text" style="left:612px;top:3498px">Letrst Collection</a>
<a class="foot-text" style="left:612px;top:3529px">Popular Colection</a>
<a class="foot-text" style="left:612px;top:3560px">Trams &amp; Condition</a>
<a class="foot-text" style="left:612px;top:3592px">Privacy &amp; Policy</a>
<div class="foot-text foot-small" style="left:754px;top:3498px;display:flex;gap:6px">
  <svg width="9" height="12" viewBox="0 0 9 12"><path d="M4.5 11S1 7 1 4.5a3.5 3.5 0 0 1 7 0C8 7 4.5 11 4.5 11z" fill="none" stroke="#fff"/><circle cx="4.5" cy="4.5" r="1.2" fill="#fff"/></svg>
  <span>Brindle Street 48<br>214 60 Tarnvik</span>
</div>
<div class="foot-text foot-small" style="left:754px;top:3544px;display:flex;gap:6px;align-items:center">
  <svg width="10" height="8" viewBox="0 0 10 8"><rect x=".5" y=".5" width="9" height="7" fill="none" stroke="#fff"/><path d="M.5.5 5 4.5 9.5.5" fill="none" stroke="#fff"/></svg>
  <span>support@Varrow.se</span>
</div>
<div class="abs foot-dot" style="left:772px;top:3576px"><svg width="8" height="10"><text x="4" y="9" text-anchor="middle" font-size="9" font-weight="700" fill="#fff" font-family="Lato,sans-serif">f</text></svg></div>
<div class="abs foot-dot" style="left:810px;top:3576px"><svg width="10" height="10" viewBox="0 0 10 10"><rect x="1" y="1" width="8" height="8" rx="2.2" fill="none" stroke="#fff"/><circle cx="5" cy="5" r="1.8" fill="none" stroke="#fff"/></svg></div>

<div class="abs" style="left:183px;top:3663px;width:834px;height:1px;background:var(--rule)"></div>
<div class="foot-text" style="left:183px;top:3678px;font-size:9px">© Copyright@Halvern | All Rights Reserved</div>
<div class="foot-text" style="left:955px;top:3678px;font-size:9px;display:flex;align-items:center;gap:3px">Language
  <svg width="9" height="9" viewBox="0 0 10 10"><circle cx="5" cy="5" r="4" fill="none" stroke="#fff"/><path d="M1 5h8M5 1c2 2 2 6 0 8M5 1c-2 2-2 6 0 8" fill="none" stroke="#fff" stroke-width=".7"/></svg>
  <svg width="6" height="4"><path d="M0 0h6L3 4z" fill="#fff"/></svg>
</div>
</body>
</html>
```